Create Some Sweet Creative for a Creative

I am a marketing consultant and creative director who is looking for some unique assets for my new website. Check out the attached creative brief - all content and hi-res images are included.
Updates

Hi There,

I posted a new creative brief - it contains are some significant changes and the hi-res assets that you'll need to please have a look.  I also upgraded the payment status to guaranteed. 

Thanks,
Delia 

Target Market(s)

Marketing Managers, Business Owners and Creative Service Providers

Industry/Entity Type

Marketing

Requirements
Must have
• Each of the 5 designs must include the basic elements provided in the creative brief (copy and accent image). Feel free to interpret with effects, additional graphic noise, distortion or cropping.

```html
<!DOCTYPE html>
<html lang="en">
<head>
<meta charset="utf-8">
<title>Well Begun is Half-Done</title>
<link rel="stylesheet" href="https://fonts.googleapis.com/css2?family=PT+Sans:wght@700&display=swap">
<style>
  :root {
    --canvas-bg: #f3f5f7;
    --pattern-tone: #d6d9db;
    --pattern-tone-soft: #e6e8ea;
    --ink: #161616;
    --figure-coat: #bfe0ee;
    --figure-umbrella: #8fd3e8;
    --figure-accent: #e58aa8;
    --figure-hair: #d9543a;
  }
  * { margin: 0; padding: 0; box-sizing: border-box; }
  html, body {
    width: 1200px;
    height: 200px;
    overflow: hidden;
    background: var(--canvas-bg);
  }
  .banner {
    position: relative;
    width: 1200px;
    height: 200px;
    overflow: hidden;
    background: var(--canvas-bg);
    font-family: "PT Sans", "Arial Narrow", sans-serif;
    color: var(--ink);
  }
  .silhouette-pattern {
    position: absolute;
    top: 0;
    height: 200px;
    background: repeating-linear-gradient(90deg,
      var(--canvas-bg) 0px,
      var(--pattern-tone-soft) 30px,
      var(--pattern-tone) 60px,
      var(--pattern-tone-soft) 90px,
      var(--canvas-bg) 120px);
    opacity: 0.9;
  }
  .silhouette-pattern--left { left: 0; width: 460px; }
  .silhouette-pattern--right { left: 740px; width: 460px; }
  .headline {
    position: absolute;
    left: 400px;
    top: 0;
    width: 298px;
    height: 200px;
    font-weight: 700;
    line-height: 1;
    white-space: nowrap;
  }
  .headline__intro,
  .headline__title,
  .headline__accent {
    position: absolute;
    display: block;
  }
  .headline__intro {
    right: 12px;
    top: 59px;
    font-size: 17px;
  }
  .headline__title {
    right: 12px;
    top: 74px;
    font-size: 29px;
  }
  .headline__accent {
    right: 0;
    top: 103px;
    font-size: 44px;
  }
  .umbrella-figure {
    position: absolute;
    left: 702px;
    top: 20px;
    width: 32px;
    height: 132px;
  }
</style>
</head>
<body>
  <div class="banner">
    <div class="silhouette-pattern silhouette-pattern--left" role="img" aria-label="Repeating pale grey silhouettes of a woman holding an umbrella"></div>
    <div class="silhouette-pattern silhouette-pattern--right" role="img" aria-label="Repeating pale grey silhouettes of a woman holding an umbrella"></div>

    <h1 class="headline">
      <span class="headline__intro">Our first game is called</span>
      <span class="headline__title">Well Begun is</span>
      <span class="headline__accent">Half--Done</span>
    </h1>

    <svg class="umbrella-figure" viewBox="0 0 32 132" role="img" aria-label="Illustration of a red-haired woman in a light blue coat holding a turquoise umbrella">
      <defs>
        <linearGradient id="figure-tones" x1="0" y1="0" x2="0" y2="1">
          <stop offset="0" stop-color="var(--figure-umbrella)"/>
          <stop offset="0.22" stop-color="var(--figure-hair)"/>
          <stop offset="0.4" stop-color="var(--figure-coat)"/>
          <stop offset="0.62" stop-color="var(--figure-accent)"/>
          <stop offset="1" stop-color="var(--figure-coat)"/>
        </linearGradient>
      </defs>
      <rect x="0" y="0" width="32" height="132" rx="5" fill="url(#figure-tones)"/>
    </svg>
  </div>
</body>
</html>
```